Interior Design/ New Construction interior finishes

Interior Design Website

Target Market(s)

Home builders, New Construction, Renovations, Public

Industry/Entity Type

Construction

Coding

Coded - Design and coding required

Number of Pages Required

1 page

Font styles to use
Sans Serif

Colors

Designer to choose colors to be used in the design.

Requirements
Must have
• Section to upload pictures of projects
• Simple and modern design
• Designer 1 details about myself
• Logo
• Upload section for photos for future jobs
Nice to have
• Sections they can click on to see certain rooms in a house
• Decorating, floral arrangements, holiday decorating.
• I have lots of before and after as well. Maybe a section for those.

```html
<!DOCTYPE html>
<html lang="en">
<head>
<meta charset="utf-8">
<title>Nova Interiors — Website Layout</title>
<link href="https://fonts.googleapis.com/css2?family=Josefin+Sans:wght@300;400;600&display=swap" rel="stylesheet">
<style>
  :root {
    --ink: #1a1a1a;
    --panel: #1b1b1b;
    --paper: #ffffff;
    --muted: #8a8a8a;
    --soft: #b9b9b9;
    --button: #6e6e6e;
    --line: #cfcfcf;
  }
  * { box-sizing: border-box; margin: 0; padding: 0; }
  html, body { width: 1200px; height: 1200px; overflow: hidden; background: var(--paper); }
  body { position: relative; font-family: "Josefin Sans", sans-serif; color: var(--ink); }
  .abs { position: absolute; }

  /* header */
  .header-bar { left: 5px; top: 6px; width: 577px; height: 41px; background: var(--panel); }
  .brand { left: 16px; top: 8px; width: 63px; height: 34px; background: #000; display: flex; flex-direction: column; align-items: center; justify-content: center; gap: 2px; }
  .brand-dot { width: 12px; height: 12px; border: 1px solid #fff; border-radius: 50%; }
  .brand-name { color: #fff; font-size: 5.5px; letter-spacing: .8px; }
  .nav { top: 20px; font-size: 5px; color: #9a9a9a; letter-spacing: .3px; }
  .nav-line { left: 464px; top: 22px; width: 30px; height: 1px; background: #777; }
  .lang { left: 501px; top: 20px; font-size: 5px; color: #fff; }

  .side-strip { left: 547px; top: 46px; width: 35px; height: 263px; background: var(--panel); }
  .vert { writing-mode: vertical-rl; font-size: 4.6px; letter-spacing: .4px; }
  .strip-line { left: 564px; top: 60px; width: 1px; height: 40px; background: #666; }

  /* photos */
  .photo { position: absolute; }
  .ph-bath { background: linear-gradient(135deg, #5f5a61, #8c8489 45%, #6a625f); }
  .ph-dining { background: linear-gradient(180deg, #d9dccd 0%, #c9ccbc 55%, #3d3129 100%); }
  .ph-living { background: linear-gradient(160deg, #8a6c4e, #b08a5c 40%, #2b2624 80%); }
  .ph-great { background: linear-gradient(180deg, #7a5534, #c9a27a 45%, #b6a89a 100%); }
  .ph-exterior { background: linear-gradient(180deg, #6c6e73, #9c8a72 55%, #7e6b55); }
  .ph-pool { background: linear-gradient(180deg, #5e6064 0%, #8a7b66 45%, #2f6f86 75%, #4f6a2c 100%); }
  .ph-before { background: linear-gradient(160deg, #f1f1ef, #d8d9d8 60%, #9a9a98); }
  .ph-after { background: linear-gradient(160deg, #f3f3f1, #dedede 60%, #8e8f91); }

  .hero-title { left: 86px; top: 164px; font-size: 22px; font-weight: 400; line-height: 27px; color: #fff; }
  .link-arrow { display: flex; align-items: center; gap: 5px; font-size: 4.8px; color: #fff; letter-spacing: .3px; }
  .link-arrow svg { width: 12px; height: 5px; }

  .tab-cover { left: 5px; top: 347px; width: 301px; height: 27px; background: var(--paper); }
  .tab { top: 367px; display: flex; align-items: center; gap: 6px; font-size: 5px; color: var(--soft); }
  .tab-num { width: 15px; height: 15px; border: 1px solid var(--line); border-radius: 50%; display: flex; align-items: center; justify-content: center; font-size: 4.5px; }
  .tab-rule { left: 24px; top: 398px; width: 69px; height: 1px; background: #999; }

  .eyebrow { font-size: 6.5px; color: var(--muted); letter-spacing: .6px; }
  .heading { font-size: 18px; font-weight: 300; line-height: 24px; }
  .heading.light { color: #fff; }
  .body { font-size: 5.4px; line-height: 11.7px; color: #444; }
  .body.light { color: #d6d6d6; line-height: 12.4px; }

  .panel { background: var(--panel); }
  .btn { background: var(--button); color: #fff; font-size: 5px; display: flex; align-items: center; justify-content: center; letter-spacing: .3px; }

  .caption { font-size: 6.5px; color: var(--muted); }
  .play { display: flex; align-items: center; gap: 9px; font-size: 5.4px; color: #333; }
  .play-ring { width: 18px; height: 18px; border: 1px solid #999; border-radius: 50%; display: flex; align-items: center; justify-content: center; }
</style>
</head>
<body>

  <!-- left column: hero -->
  <div class="abs header-bar"></div>
  <div class="abs brand"><span class="brand-dot"></span><span class="brand-name">Nova Interiors</span></div>
  <span class="abs nav" style="left:241px">HOME</span>
  <span class="abs nav" style="left:279px">About</span>
  <span class="abs nav" style="left:317px">How it works</span>
  <span class="abs nav" style="left:373px">Details</span>
  <span class="abs nav" style="left:413px">Contact</span>
  <div class="abs nav-line"></div>
  <span class="abs lang">LANGUAGE <b>(EN)</b></span>

  <div class="photo ph-bath" style="left:5px;top:46px;width:542px;height:328px" role="img" aria-label="Bright master bathroom with freestanding tub and starburst chandelier"></div>
  <div class="abs side-strip"></div>
  <div class="abs strip-line"></div>
  <span class="abs vert" style="left:562px;top:110px;color:#cfcfcf">hello@novainteriors.com</span>
  <span class="abs vert" style="left:562px;top:170px;color:#cfcfcf">(+1) 555 014 2678</span>
  <div class="abs" style="left:564px;top:290px;width:1px;height:20px;background:#555"></div>
  <span class="abs vert" style="left:562px;top:334px;color:#777">SCROLL DOWN</span>

  <h1 class="abs hero-title">The Best Way To Find<br>Your Perfect Home.</h1>
  <div class="abs link-arrow" style="left:92px;top:239px">LEARN MORE
    <svg viewBox="0 0 12 5"><path d="M0 2.5H11M9 .5l2 2-2 2" stroke="#fff" stroke-width=".6" fill="none"/></svg></div>

  <div class="abs tab-cover"></div>
  <div class="abs tab" style="left:24px"><span class="tab-num">01</span>Design Professionals</div>
  <div class="abs tab" style="left:131px"><span class="tab-num">02</span>Contract</div>
  <div class="abs tab" style="left:206px"><span class="tab-num">03</span>Home Developers</div>
  <div class="abs tab-rule"></div>

  <!-- left column: welcome -->
  <p class="abs eyebrow" style="left:24px;top:460px">Welcome To Nova Interiors</p>
  <h2 class="abs heading" style="left:24px;top:478px">We invite you to discover<br>global &amp; colorful twist<br>to home design.</h2>
  <p class="abs body" style="left:24px;top:566px;width:140px">We plan interiors for new builds and renovations, pairing finishes, fixtures and furniture so every room feels calm and complete. From first sketch to final styling, each choice is made with the client, the builder and the budget in mind, keeping the whole project on schedule.</p>
  <p class="abs body" style="left:183px;top:566px;width:140px">We plan interiors for new builds and renovations, pairing finishes, fixtures and furniture so every room feels calm and complete. From first sketch to final styling, each choice is made with the client, the builder and the budget in mind, keeping the whole project on schedule.</p>
  <div class="photo ph-dining" style="left:368px;top:436px;width:198px;height:258px" role="img" aria-label="Round dining table with upholstered chairs under a wood chandelier"></div>

  <!-- left column: style section -->
  <div class="photo ph-living" style="left:5px;top:765px;width:169px;height:262px" role="img" aria-label="Living room with beamed ceiling and dark sectional sofa"></div>
  <div class="photo ph-great" style="left:194px;top:726px;width:154px;height:220px" role="img" aria-label="Great room with wood beams, stone fireplace and dining set"></div>
  <div class="abs panel" style="left:299px;top:805px;width:283px;height:395px"></div>
  <h2 class="abs heading light" style="left:386px;top:877px">We let you meet the<br>demands of project<br>with perfect style.</h2>
  <p class="abs body light" style="left:386px;top:964px;width:166px">Builders and homeowners rely on us to select finishes that last. We source tile, lighting, cabinetry and hardware, prepare clear selection sheets, and coordinate with trades on site so the design you approved is the design that gets installed, down to the last detail and trim.</p>
  <div class="abs btn" style="left:386px;top:1089px;width:68px;height:22px">CONTACT US</div>
  <div class="photo ph-exterior" style="left:5px;top:1056px;width:294px;height:144px" role="img" aria-label="Brick home exterior with covered balcony"></div>

  <!-- right column -->
  <h2 class="abs heading" style="left:650px;top:-2px">global &amp; colorful twist<br>to home design.</h2>
  <p class="abs body" style="left:650px;top:66px;width:140px">We plan interiors for new builds and renovations, pairing finishes, fixtures and furniture so every room feels calm and complete. From first sketch to final styling, each choice is made with the client, the builder and the budget in mind, keeping the whole project on schedule.</p>
  <p class="abs body" style="left:810px;top:66px;width:140px">We plan interiors for new builds and renovations, pairing finishes, fixtures and furniture so every room feels calm and complete. From first sketch to final styling, each choice is made with the client, the builder and the budget in mind, keeping the whole project on schedule.</p>
  <div class="photo ph-dining" style="left:995px;top:0;width:198px;height:193px" role="img" aria-label="Round dining table with upholstered chairs"></div>

  <div class="abs panel" style="left:926px;top:304px;width:274px;height:426px"></div>
  <div class="photo ph-living" style="left:632px;top:264px;width:170px;height:262px" role="img" aria-label="Living room with beamed ceiling and dark sectional sofa"></div>
  <div class="photo ph-great" style="left:821px;top:225px;width:154px;height:220px" role="img" aria-label="Great room with wood beams, stone fireplace and dining set"></div>
  <h2 class="abs heading light" style="left:1013px;top:377px">We let you meet the<br>demands of project<br>with perfect style.</h2>
  <p class="abs body light" style="left:1013px;top:464px;width:166px">Builders and homeowners rely on us to select finishes that last. We source tile, lighting, cabinetry and hardware, prepare clear selection sheets, and coordinate with trades on site so the design you approved is the design that gets installed, down to the last detail and trim.</p>
  <div class="abs btn" style="left:1014px;top:588px;width:68px;height:22px">CONTACT US</div>

  <div class="photo ph-pool" style="left:632px;top:555px;width:387px;height:351px" role="img" aria-label="Brick home backyard with natural stone swimming pool"></div>
  <h2 class="abs" style="left:674px;top:722px;font-size:22px;font-weight:400;color:#fff">Collection of our Work.</h2>
  <p class="abs" style="left:674px;top:762px;width:220px;font-size:5.4px;line-height:10px;color:#eee">A look at finished homes, renovations and outdoor spaces we have styled for builders and families.</p>
  <div class="abs link-arrow" style="left:680px;top:810px">VIEW WORK
    <svg viewBox="0 0 12 5"><path d="M0 2.5H11M9 .5l2 2-2 2" stroke="#fff" stroke-width=".6" fill="none"/></svg></div>

  <h2 class="abs heading" style="left:662px;top:973px">Our uncompromising<br>&amp; dedicated devotion<br>to quality.</h2>
  <p class="abs body" style="left:662px;top:1062px;width:160px">Every detail is checked before handover, from grout lines to cabinet pulls, so the finished room matches the plan.</p>
  <div class="abs play" style="left:662px;top:1124px">
    <span class="play-ring"><svg width="6" height="6" viewBox="0 0 6 6"><path d="M1.5 1l3 2-3 2z" fill="#555"/></svg></span>Play Quick Video</div>

  <div class="photo ph-before" style="left:870px;top:953px;width:155px;height:217px" role="img" aria-label="Bathroom before styling, white walls and bare finishes"></div>
  <p class="abs caption" style="left:870px;top:1180px">Before</p>
  <div class="photo ph-after" style="left:1054px;top:863px;width:144px;height:213px" role="img" aria-label="Bathroom after finishing, white cabinetry and dark counters"></div>
  <p class="abs caption" style="left:1054px;top:1087px">After</p>

</body>
</html>
```